KESTREL clinical trial results infographic

We need an infographic which presents the results from the KESTREL research trial. It should be colourful and engaging, in understandable language and showing the steps to get to the results. This is to showcase the results to patients/the public/clinicians, giving a brief summary of what the study proved. The final design should have the KESTREL logo at the top (please see attached and https://kestrel.vanmoretrials.example/)
I have attached the required logos which need to be used (KESTREL, Halbrook Injury and Acute Medicine, University of Tarnwell) as well as an example from another study, PLOVEN3, as an example of what the layout could look like. Please DO NOT use the content from the PLOVEN3 example though, please instead use the content from the attached document 'KESTREL_InfographicDesignInformation_ArtPoolHub'. Please also include information about the funding in a footer at the bottom of the infographic (as per the above document).
Updates

```html
<!DOCTYPE html>
<html lang="en">
<head>
<meta charset="utf-8">
<title>KESTREL Study Presentation</title>
<link rel="stylesheet" href="https://fonts.googleapis.com/css2?family=Lato:wght@400;700;900&family=Rubik:wght@400;500;700&display=swap">
<style>
  :root {
    --cyan: #0fc1e0;
    --purple: #c96ae3;
    --navy: #0d1b45;
    --steel: #2f5f99;
    --mist: #ccd8e8;
    --ink: #111111;
    --white: #ffffff;
  }
  * { box-sizing: border-box; margin: 0; padding: 0; }
  html, body { width: 848px; height: 1200px; overflow: hidden; background: var(--white); }
  body { font-family: "Rubik", sans-serif; color: var(--ink); }
  .canvas { position: relative; width: 848px; height: 1200px; overflow: hidden; background: var(--white); }
  .abs { position: absolute; }

  .dot-texture { left: 0; top: 0; width: 200px; height: 230px;
    background: radial-gradient(circle at 0 0, rgba(201,106,227,0.22), rgba(201,106,227,0) 70%); }

  .brand-mark { left: 78px; top: 44px; display: flex; align-items: center; gap: 10px; }
  .brand-mark .dot { width: 20px; height: 20px; border-radius: 50%; background: var(--steel); }
  .brand-mark .name { font-family: "Lato", sans-serif; font-weight: 900; font-size: 52px; color: var(--steel); letter-spacing: 1px; }

  .uni-badge { left: 643px; top: 0; width: 117px; height: 122px; background: var(--navy);
    border: 4px solid var(--purple); border-top: none; display: flex; align-items: flex-end; padding: 0 8px 12px; }
  .uni-badge span { font-family: "Lato", sans-serif; font-weight: 400; color: var(--white); font-size: 15px; line-height: 1.15; }

  .kicker { left: 0; width: 848px; top: 143px; text-align: center; color: var(--steel); font-size: 13.5px; }
  .title-pill { left: 218px; top: 175px; width: 409px; height: 42px; border-radius: 21px; background: var(--purple);
    color: var(--white); font-family: "Lato", sans-serif; font-weight: 700; font-size: 29px; text-align: center; line-height: 42px; }
  .intro { left: 124px; width: 600px; top: 226px; text-align: center; font-size: 13.5px; line-height: 19.2px; }
  .swoosh { left: 0; top: 255px; }

  .section-title { font-family: "Lato", sans-serif; font-weight: 400; }
  .pain-title { left: 78px; top: 384px; font-size: 23px; }
  .focus-item { left: 78px; width: 214px; height: 52px; }
  .focus-item .pill { position: absolute; left: 30px; right: 0; top: 3px; bottom: 3px; border-radius: 0 10px 10px 0;
    border: 3px solid var(--purple); display: flex; align-items: center; justify-content: flex-end; padding-right: 10px;
    text-align: right; font-size: 13px; line-height: 18px; background: var(--white); }
  .focus-item .badge { position: absolute; left: 0; top: 0; width: 54px; height: 54px; border-radius: 50%;
    border: 3px solid var(--navy); background: var(--white); display: flex; align-items: center; justify-content: center; z-index: 1; }
  .focus-item .badge i { width: 40px; height: 40px; border-radius: 50%; background: var(--cyan); }
  .focus-item.alt .pill { border-color: var(--navy); }
  .focus-item.alt .badge { border-color: var(--cyan); }
  .focus-item.alt .badge i { background: var(--purple); }

  .figure-slot { left: 318px; top: 388px; width: 122px; height: 170px; border-radius: 50px 50px 6px 6px;
    background: linear-gradient(180deg, rgba(15,193,224,0.12), rgba(15,193,224,0.55)); }

  .design-title { right: 86px; top: 386px; font-size: 25px; text-align: right; }
  .design-sub { right: 86px; top: 425px; font-size: 12.5px; line-height: 17px; text-align: right; }
  .timeline { left: 444px; top: 471px; width: 320px; display: flex; }
  .timeline .step { flex: 1; position: relative; }
  .timeline .label { height: 24px; background: var(--mist); font-weight: 700; font-size: 11px; text-align: center; line-height: 24px; }
  .timeline .step.done .label { background: var(--purple); color: var(--white); }
  .timeline .stem { width: 2px; height: 24px; background: var(--cyan); margin: 0 auto; }
  .timeline .note { font-size: 8px; line-height: 11px; text-align: center; margin-top: 15px; padding: 0 8px; }

  .rule { left: 69px; width: 705px; height: 0; border-top: 4px dashed var(--cyan); }
  .rule.purple { border-top-color: var(--purple); }

  .elig-title { left: 0; width: 848px; top: 615px; text-align: center; font-size: 27px; }
  .rule-card { border: 4px solid var(--cyan); border-radius: 40px; background: var(--white); padding: 14px 10px 0 10px; }
  .rule-card h3 { font-family: "Lato", sans-serif; font-weight: 400; font-size: 17px; margin-bottom: 6px; }
  .rule-card p { font-size: 10.8px; line-height: 16px; }
  .rule-card.right { text-align: right; }
  .rule-card.right h3 { text-align: center; padding-left: 60px; }
  .fill-card { background: var(--purple); color: var(--white); border-radius: 38px; padding: 12px 18px; }
  .fill-card h3 { font-family: "Lato", sans-serif; font-weight: 400; font-size: 17px; margin-bottom: 6px; }
  .fill-card p { font-size: 10.8px; line-height: 15.5px; }
  .fill-card.right { text-align: right; }
  .icon-inline { display: inline-block; vertical-align: -2px; }

  .corner-arc { background: var(--cyan); overflow: hidden; }
  .corner-arc::after { content: ""; position: absolute; width: 200%; height: 110%; border-radius: 50%; background: var(--white); top: -5%; }
  .key-arc { left: 80px; top: 882px; width: 75px; height: 116px; }
  .key-arc::after { left: 6px; }
  .key-text { left: 104px; top: 914px; }
  .key-text h2 { font-family: "Lato", sans-serif; font-weight: 400; font-size: 21px; }
  .key-text p { font-size: 14px; line-height: 19px; margin-top: 1px; }

  .stat-card { top: 892px; width: 153px; height: 106px; color: var(--white); padding: 8px 14px; }
  .stat-card.cyan { left: 390px; background: var(--cyan); }
  .stat-card.purple { left: 609px; background: var(--purple); }
  .stat-card .value { font-weight: 700; font-size: 12px; }
  .stat-card .bar { display: flex; height: 10px; margin-top: 22px; }
  .stat-card .bar .done { width: 58%; background: var(--white); }
  .stat-card .bar .rest { flex: 1; }
  .stat-card.cyan .bar .rest { background: var(--purple); }
  .stat-card.purple .bar .rest { background: var(--cyan); }
  .stat-card .legend { display: flex; justify-content: space-between; align-items: flex-end; margin-top: 18px; font-size: 6.5px; line-height: 9px; }
  .stat-card .legend b { font-weight: 700; }
  .stat-card .legend span { text-align: right; }

  .rule.short { left: 184px; width: 474px; top: 1026px; }

  .contact-chip { top: 1066px; width: 162px; height: 48px; background: var(--mist); display: flex; }
  .contact-chip .text { flex: 1; padding: 10px 0 0 8px; }
  .contact-chip h4 { font-weight: 700; font-size: 13.5px; }
  .contact-chip small { display: block; font-size: 6.5px; margin-top: 4px; }
  .contact-chip small.link { text-decoration: underline; }
  .contact-chip .tile { width: 44px; height: 44px; margin: 2px; background: var(--cyan); display: flex; align-items: center; justify-content: center; }
  .contact-chip .tile i { width: 32px; height: 32px; border-radius: 10px; background: var(--mist); }
  .contact-chip.email { background: #c3cfe2; }

  .contact-arc { left: 700px; top: 1030px; width: 62px; height: 113px; }
  .contact-arc::after { right: 6px; }
  .contact-title { right: 106px; top: 1062px; text-align: right; font-size: 21px; line-height: 24px; }

  .funding-footer { left: 0; top: 1158px; width: 848px; height: 42px; background: var(--navy); color: var(--white);
    display: flex; align-items: center; justify-content: space-between; padding: 0 79px; font-size: 9px; line-height: 12px; }
  .funding-footer .partner { display: flex; align-items: center; gap: 6px; font-size: 11px; font-weight: 500; }
  .funding-footer .partner i { width: 10px; height: 10px; border-radius: 50%; background: var(--cyan); }
</style>
</head>
<body>
<main class="canvas">
  <div class="abs dot-texture" role="img" aria-label="Soft dotted texture in the top corner"></div>

  <header>
    <div class="abs brand-mark"><span class="dot"></span><span class="name">KESTREL</span></div>
    <div class="abs uni-badge"><span>University of Tarnwell</span></div>
    <p class="abs kicker">A Pilot Study on Shoulder Pain Treatments</p>
    <h1 class="abs title-pill">KESTREL Study Presentation</h1>
    <p class="abs intro">Shoulder pain is common, often caused by inflammation under the shoulder.<br>The KESTREL study compares a biologic injection (using parts of a patient’s own<br>blood) with a steroid injection to see which works better for shoulder pain.<br>This is a pilot study with 50 patients to test if the process works well and if<br>patients and doctors are happy with it.</p>
    <svg class="abs swoosh" width="848" height="110" viewBox="0 0 848 110" aria-hidden="true">
      <path d="M0 13 Q424 185 848 19" fill="none" stroke="var(--purple)" stroke-width="5"/>
    </svg>
  </header>

  <section>
    <h2 class="abs section-title pain-title">Shoulder Pain Study</h2>
    <div class="abs focus-item" style="top:437px;">
      <div class="badge"><i></i></div>
      <div class="pill">Comparing biologic<br>and steroid injections</div>
    </div>
    <div class="abs focus-item alt" style="top:503px;">
      <div class="badge"><i></i></div>
      <div class="pill">Focus on patient<br>recovery and satisfactio</div>
    </div>

    <div class="abs figure-slot" role="img" aria-label="Line illustration of a person seen from behind holding a painful shoulder"></div>

    <h2 class="abs section-title design-title">Study Design</h2>
    <p class="abs design-sub">Overview of the KESTREL Study<br>Timeline and Key Milestones</p>
    <div class="abs timeline">
      <div class="step"><div class="label">Recruitment</div><div class="stem"></div><p class="note">Participants recruited over 7 months.</p></div>
      <div class="step"><div class="label">Follow-up</div><div class="stem"></div><p class="note">50 patients involved in the study.</p></div>
      <div class="step done"><div class="label">Study completion</div><div class="stem"></div><p class="note">6 months of patient follow-up.</p></div>
    </div>
  </section>

  <div class="abs rule" style="top:597px;"></div>

  <section>
    <h2 class="abs section-title elig-title">Eligibility Criteria for KESTREL Study</h2>

    <div class="abs fill-card" style="left:132px; top:757px; width:251px; height:75px; padding-top:22px;">
      <h3 style="margin-top:-8px;">Additional Criteria</h3>
      <p>Must not be pregnant or breastfeeding, and have no allergies to study injections.</p>
    </div>
    <div class="abs rule-card" style="left:140px; top:665px; width:235px; height:97px;">
      <h3>Inclusion (<svg class="icon-inline" width="16" height="16" viewBox="0 0 16 16" aria-hidden="true"><rect width="16" height="16" rx="3" fill="#5cb82e"/><path d="M4 8.5l3 3 5-6" fill="none" stroke="#fff" stroke-width="2"/></svg>)</h3>
      <p>Participants must be adults experiencing shoulder pain for at least three months.</p>
    </div>

    <div class="abs fill-card right" style="left:436px; top:757px; width:274px; height:78px; padding-top:22px;">
      <h3 style="margin-top:-8px;">Study Requirements</h3>
      <p>Participants should be willing to attend follow-up appointments and provide feedback.</p>
    </div>
    <div class="abs rule-card right" style="left:449px; top:669px; width:251px; height:97px;">
      <h3>Exclusion (<svg class="icon-inline" width="16" height="16" viewBox="0 0 16 16" aria-hidden="true"><path d="M2 2l12 12M14 2L2 14" stroke="#d8434b" stroke-width="2.4"/></svg>)</h3>
      <p>Individuals with previous shoulder surgery or severe medical conditions are not eligible.</p>
    </div>
  </section>

  <div class="abs rule purple" style="top:860px;"></div>

  <section>
    <div class="abs corner-arc key-arc"></div>
    <div class="abs key-text">
      <h2>Key Messages</h2>
      <p>Highlights from the KESTREL study on<br>shoulder pain treatments</p>
    </div>
    <div class="abs stat-card cyan">
      <div class="value">80%</div>
      <div class="bar"><span class="done"></span><span class="rest"></span></div>
      <div class="legend"><b>SUCCESS RATE</b><span>Likelihood of<br>effective treatment</span></div>
    </div>
    <div class="abs stat-card purple">
      <div class="value">50%</div>
      <div class="bar"><span class="done"></span><span class="rest"></span></div>
      <div class="legend"><b>PARTICIPANTS<br>RECRUITED</b><span>Total number of<br>patients</span></div>
    </div>
  </section>

  <div class="abs rule short"></div>

  <section>
    <div class="abs contact-chip" style="left:79px;">
      <div class="text"><h4>Main Contact</h4><small class="link">Mirela Ostrander</small></div>
      <div class="tile"><i></i></div>
    </div>
    <div class="abs contact-chip" style="left:251px;">
      <div class="text"><h4>Phone</h4><small>01632-960417</small></div>
      <div class="tile"><i style="border-radius:50%;"></i></div>
    </div>
    <div class="abs contact-chip email" style="left:422px;">
      <div class="text"><h4>Email</h4><small>kestrel@hiam.tarnwell.example</small></div>
      <div class="tile"><i style="border-radius:6px;"></i></div>
    </div>
    <div class="abs corner-arc contact-arc"></div>
    <h2 class="abs section-title contact-title">Contact<br>Information</h2>
  </section>

  <footer class="abs funding-footer">
    <span class="partner"><i></i>Halbrook Injury and Acute Medicine</span>
    <span>Funded by the Vanmore Health Research Foundation.<br>Views expressed are those of the KESTREL study team.</span>
  </footer>
</main>
</body>
</html>
```